Manufacturers Catalog Cover Page

We are looking to have a cover to our catalog page designed. I currently have begun work for the remained of the catalog in InDesign and want the cover created in InDesign. I will provide photos.

Looking to beable to add the cover to our existing attached catalog.

Industry/Entity Type

Manufacturing

Requirements
Must have
• Colors match what we are currently using. The Dark grey and gold
Nice to have
• modern, clean

```html
<!DOCTYPE html>
<html lang="en">
<head>
<meta charset="utf-8">
<title>Keystone Elastics — Catalog Cover</title>
<link rel="stylesheet" href="https://fonts.googleapis.com/css2?family=Bebas+Neue&display=swap">
<style>
  :root {
    --charcoal: #414143;
    --charcoal-deep: #2f2f31;
    --gold: #d4b57a;
    --white: #ffffff;
  }
  * { margin: 0; padding: 0; box-sizing: border-box; }
  html, body {
    width: 848px;
    height: 1200px;
    overflow: hidden;
    background: var(--charcoal);
  }
  .cover {
    position: relative;
    width: 848px;
    height: 1200px;
    background: var(--charcoal);
    font-family: "Bebas Neue", "Oswald", sans-serif;
    overflow: hidden;
  }
  .cover__texture {
    position: absolute;
    left: 0; top: 0;
    width: 848px;
    height: 620px;
    background:
      radial-gradient(ellipse 520px 300px at 320px 200px, rgba(20,20,22,0.55), transparent 70%),
      radial-gradient(ellipse 380px 200px at 700px 420px, rgba(25,25,27,0.4), transparent 70%),
      linear-gradient(180deg, var(--charcoal-deep) 0%, var(--charcoal) 100%);
    opacity: 0.9;
  }
  .brand {
    position: absolute;
    left: 182px;
    top: 62px;
  }
  .brand__name {
    color: var(--white);
    font-size: 46px;
    line-height: 52px;
    letter-spacing: 0.5px;
  }
  .headline {
    position: absolute;
    left: 0;
    width: 848px;
    text-align: center;
    color: var(--gold);
    line-height: 1.2;
  }
  .headline__kicker {
    top: 364px;
    font-size: 68px;
    letter-spacing: 0.5px;
  }
  .headline__main {
    top: 452px;
    font-size: 95px;
    letter-spacing: 0.5px;
  }
  .sector {
    position: absolute;
    top: 686px;
    width: 179px;
    height: 179px;
    border-radius: 16px;
    border: 1.5px solid var(--gold);
  }
  .sector--auto {
    left: 86px;
    background: linear-gradient(180deg, #7fa7d3 0%, #c7d6e4 45%, #a8a9a6 60%, #5d5a52 100%);
  }
  .sector--industrial {
    left: 334px;
    background: linear-gradient(180deg, #9fb5cf 0%, #c9b04a 50%, #8a8f96 100%);
  }
  .sector--commercial {
    left: 582px;
    background: linear-gradient(180deg, #8db2dc 0%, #d5d6d2 40%, #a9b2ae 70%, #5f7b4e 100%);
  }
  .contact {
    position: absolute;
    right: 54px;
    top: 1048px;
    text-align: right;
    color: var(--white);
  }
  .contact__phone {
    font-size: 26px;
    line-height: 31px;
    letter-spacing: 0.3px;
  }
  .contact__web {
    margin-top: 2px;
    font-size: 34px;
    line-height: 40px;
    letter-spacing: 0.3px;
  }
</style>
</head>
<body>
  <main class="cover">
    <div class="cover__texture" role="img" aria-label="Faint photo of coiled black rubber extrusion profiles"></div>

    <header class="brand">
      <div class="brand__name">Keystone<br>Elastics</div>
    </header>

    <h2 class="headline headline__kicker">Rubber &amp; Plastic Extursion</h2>
    <h1 class="headline headline__main">Gaskets, Trims &amp; Seals</h1>

    <div class="sector sector--auto" role="img" aria-label="Photo of a silver hatchback car on an open road at sunset"></div>
    <div class="sector sector--industrial" role="img" aria-label="Photo of yellow robotic arms on a factory assembly line"></div>
    <div class="sector sector--commercial" role="img" aria-label="Photo of a modern glass office building with landscaping"></div>

    <footer class="contact">
      <p class="contact__phone">888-555-0142</p>
      <p class="contact__phone">330-555-0187</p>
      <p class="contact__web">www.keystoneelastics.com</p>
    </footer>
  </main>
</body>
</html>
```